The Bright Meadow Foundation

This is a non profit . We are a 501(c)(3) charitable organization in the United States. The organization is a volunteer based group providing basic healthcare to those living in underserved rural areas around the world. I have attached a brochure that provides some information about the organization. We are looking for a basic 5 page web page Page 1 Photos that fade into the next x 3 with mission statementPage 2 About us - details about bright meadow foundation. also introducing our Founders of the organization. Marina Kellet, M.D. Dorla Penn , FNP, Rosa Tembley, FNP, Wade Marlow. ( will provide you info on each.Page 3 Projects coming up and futurePage 4 Get involved - Give a donation, Volunteer, Corporate supportPage 5 Support us and contact us with a message box.We mainly work in South America but anticipate trave to South Africa in the near future. Colors bright with emphasis on Reds and Purples. I have attached some photos and ideas. You can use or not use ok to use something similar if you so like

Target Market(s)

People interested in volunteering time or money to overseas medical work. NOT a religious base

Coding

Coded - Design and coding required

Number of Pages Required

1 page

Colors
876aae
ec1f27
f37022
9bcb3c

Requirements
Must have
• Colorful pictures nature, brings out emotion, colorful, children from various parts of the world, animals.
• Tried to down load some pictures but would not go thru.

```html
<!DOCTYPE html>
<html lang="en">
<head>
<meta charset="utf-8">
<title>Bright Meadow Foundation</title>
<link href="https://fonts.googleapis.com/css2?family=Cinzel:wght@400;700&family=Rubik:wght@400;500&display=swap" rel="stylesheet">
<style>
:root{
  --purple:#876aae;
  --purple-soft:#9a82bd;
  --red:#ec1f27;
  --red-soft:#f04a50;
  --green:#9bcb3c;
  --green-soft:#8ab834;
  --yellow:#e8c91a;
  --ink:#222;
  --muted:#666;
  --light:#f4f4f4;
  --footer:#242424;
  --white:#fff;
}
*{box-sizing:border-box;margin:0;padding:0}
html,body{width:1200px;height:3056px;overflow:hidden;background:var(--white)}
body{position:relative;font-family:'Rubik',sans-serif;color:var(--ink)}
.abs{position:absolute}
.btn{position:absolute;display:flex;align-items:center;justify-content:center;border-radius:16px;font:500 12px 'Rubik',sans-serif;letter-spacing:.3px}
.btn-red{background:var(--red);color:var(--white)}
.btn-purple{background:var(--purple);color:var(--white)}
.btn-white{background:var(--white);color:var(--purple)}
.btn-ghost{border:1.5px solid var(--white);color:var(--white)}
.btn-ghost-dark{border:1.5px solid #333;color:#222}
.heading{font-family:'Cinzel',serif;color:var(--purple);text-align:center;width:100%}

/* header */
.site-header{left:0;top:0;width:1200px;height:111px;background:var(--white)}
.brand{left:88px;top:22px;display:flex;align-items:center;gap:10px}
.brand-dot{width:42px;height:42px;border-radius:50%;background:var(--purple)}
.brand-name{font:500 22px 'Rubik',sans-serif;color:var(--purple);line-height:1.1;width:190px}
.call{left:758px;top:32px;font-size:14px;color:var(--green)}
.call span{color:var(--purple)}
.nav{top:76px;font:500 11px 'Rubik',sans-serif;letter-spacing:.4px;color:var(--ink)}
.nav.active{color:var(--purple)}

/* hero */
.hero{left:0;top:111px;width:1200px;height:486px;background:linear-gradient(180deg,#6d7d8e 0%,#8c93a4 25%,#5a6c3a 55%,#6a5aa0 75%,#4d6a2e 100%)}
.hero-line{left:0;top:595px;width:1200px;height:4px;background:var(--yellow)}
.hero-title{top:245px;width:1200px;text-align:center;font:400 54px/58px 'Cinzel',serif;color:var(--white)}

/* cards */
.card{top:567px;width:342px;height:256px;padding:52px 32px;color:var(--white)}
.card h3{font:500 20px 'Rubik',sans-serif;margin-bottom:20px}
.card p{font-size:14px;line-height:19px;width:280px}
.card .btn{left:32px;top:187px;width:128px;height:31px}
.card-art{position:absolute;right:0;bottom:0;width:96px;height:96px;border-radius:4px}

/* about */
.about-mark{left:556px;top:903px;width:88px;height:88px;border-radius:50%;background:var(--purple)}
.about-name{top:1000px;font-size:32px;line-height:34px}
.about-sub{top:1033px;font-size:20px;color:var(--green)}
.about-text{left:225px;top:1078px;width:750px;text-align:center;font-size:12.5px;line-height:21px;color:var(--muted)}

/* projects */
.projects-band{left:0;top:1305px;width:1200px;height:96px;background:var(--light)}
.projects-title{top:1330px;font-size:31px}
.project{top:1401px;width:400px;height:399px}
.project-info{left:0;top:200px;width:240px;height:199px;background:rgba(40,25,20,.55);padding:30px 32px}
.project-date{font:500 12.5px 'Rubik',sans-serif;color:var(--green);margin-bottom:10px}
.project-title{font:500 16px/19px 'Rubik',sans-serif;color:var(--white)}
.project-info .btn{left:32px;top:137px;width:80px;height:31px}

/* team */
.team-title{top:1870px;font-size:31px}
.member{top:1943px;width:232px}
.member-photo{height:271px}
.member-name{height:40px;display:flex;align-items:center;justify-content:center;font-size:14px;color:var(--purple);border-bottom:2px solid var(--purple)}
.member.active .member-name{background:var(--purple);color:var(--white)}

/* join */
.join{left:0;top:2334px;width:1200px;height:401px;background:linear-gradient(180deg,#4e6077 0%,#6a7d92 35%,#3a4c5a 70%,#2c3a42 100%)}
.join-text{left:88px;top:2450px;font:500 30px/38px 'Rubik',sans-serif;color:var(--white)}
.signup{left:88px;top:2585px;width:320px;height:39px;border:2px solid var(--white);border-radius:20px;background:var(--white)}
.signup-field{left:14px;top:11px;font-size:11px;color:#555}
.signup .btn{left:234px;top:2px;width:80px;height:31px}

/* contact band */
.contact-band{left:0;top:2735px;width:1200px;height:160px;background:var(--purple)}
.contact-title{left:190px;top:2808px;font-size:29px;color:var(--white)}
.contact-sub{left:190px;top:2846px;font-size:14px;color:var(--white)}

/* footer */
.footer{left:0;top:2895px;width:1200px;height:161px;background:var(--footer)}
.foot-link{top:2958px;font:500 11px 'Rubik',sans-serif;letter-spacing:.4px;color:#ddd}
.foot-copy{left:86px;top:2987px;font-size:11px;color:#bbb}
.social{top:2958px;width:30px;height:30px;border-radius:50%;background:var(--white)}
.to-top{left:1111px;top:2895px;width:89px;height:161px;background:var(--red)}
</style>
</head>
<body>

<header class="site-header abs">
  <div class="brand abs"><div class="brand-dot"></div><div class="brand-name">Bright Meadow Foundation</div></div>
  <div class="call abs">Call Us: <span>&#9990; 555 - 014 - 2267</span></div>
  <div class="btn btn-red" style="left:983px;top:25px;width:128px;height:30px">Donate Now!</div>
  <nav>
    <div class="nav abs active" style="left:541px">-- HOME --</div>
    <div class="nav abs" style="left:661px">ABOUT US</div>
    <div class="nav abs" style="left:777px">PROJECTS</div>
    <div class="nav abs" style="left:896px">GET INVOLVED</div>
    <div class="nav abs" style="left:1037px">CONTACT US</div>
  </nav>
</header>

<section>
  <div class="hero abs" role="img" aria-label="Mountain meadow with purple lupine flowers under a cloudy sky"></div>
  <div class="hero-line abs"></div>
  <h1 class="hero-title abs">Small Effort<br>Make Big Changes</h1>
  <div class="btn btn-white" style="left:536px;top:390px;width:128px;height:31px">Explore More</div>

  <div class="card abs" style="left:88px;background:var(--purple)">
    <h3>Give A Donation</h3>
    <p>There are many variations of passages of Lorem Ipsum available, but the majority have suffered alteration</p>
    <div class="btn btn-ghost">Donate Now!</div>
    <div class="card-art" style="background:var(--purple-soft)" role="img" aria-label="Outline illustration of a heart with a coin"></div>
  </div>
  <div class="card abs" style="left:429px;background:var(--green)">
    <h3 style="color:#222">Volunteer</h3>
    <p style="color:#222">There are many variations of passages of Lorem Ipsum available, but the majority have suffered alteration</p>
    <div class="btn btn-ghost-dark">Explore More</div>
    <div class="card-art" style="background:var(--green-soft)" role="img" aria-label="Outline illustration of a raised hand"></div>
  </div>
  <div class="card abs" style="left:770px;background:var(--red)">
    <h3>Corporate Support</h3>
    <p>There are many variations of passages of Lorem Ipsum available, but the majority have suffered alteration</p>
    <div class="btn btn-ghost">Contact Now!</div>
    <div class="card-art" style="background:var(--red-soft)" role="img" aria-label="Outline illustration of a group of people"></div>
  </div>
</section>

<section>
  <div class="about-mark abs"></div>
  <div class="heading abs about-name">Bright Meadow</div>
  <div class="heading abs about-sub">Foundation</div>
  <p class="about-text abs">Lorem Ipsum is simply dummy text of the printing and typesetting industry. Lorem Ipsum has been the industry's standard dummy text ever since the 1500s, when an unknown printer took a galley of type and scrambled it to make a type specimen book. It has survived not only five centuries, but also the leap into electronic typesetting, remaining essentially unchanged. It was popularised in the 1960s with the release of Dryline sheets ...</p>
  <div class="btn btn-purple" style="left:536px;top:1193px;width:128px;height:31px">About Us</div>
</section>

<section>
  <div class="projects-band abs"></div>
  <h2 class="heading abs projects-title">Up Coming Projects</h2>
  <div class="project abs" style="left:0;background:linear-gradient(135deg,#8a8f88,#c07a6a 50%,#7a3a2a)" role="img" aria-label="Volunteer hugging a smiling child">
    <div class="project-info abs"><div class="project-date">05 - AUG - 2019</div><div class="project-title">Contrary to popular belief, Lorem Ipsum is not simply</div><div class="btn btn-purple">More</div></div>
  </div>
  <div class="project abs" style="left:400px;background:linear-gradient(135deg,#7a6a5e,#c93a4a 45%,#8a6aa8 75%,#5a3a3a)" role="img" aria-label="Woman in colourful traditional dress holding a small child">
    <div class="project-info abs"><div class="project-date">10 - SEP - 2019</div><div class="project-title">Contrary to popular belief, Lorem Ipsum is not simply</div><div class="btn btn-red">More</div></div>
  </div>
  <div class="project abs" style="left:800px;background:linear-gradient(135deg,#a83a2a,#c8762a 45%,#6a2a1a)" role="img" aria-label="Woman wearing traditional jewellery and a red head scarf">
    <div class="project-info abs"><div class="project-date">05 - AUG - 2019</div><div class="project-title">Contrary to popular belief, Lorem Ipsum is not simply</div><div class="btn btn-purple">More</div></div>
  </div>
</section>

<section>
  <h2 class="heading abs team-title">Meet The Team</h2>
  <div class="member abs" style="left:88px"><div class="member-photo" style="background:linear-gradient(160deg,#8a8a7a,#5a6a4a 60%,#3a3a3a)" role="img" aria-label="Portrait of Marina Kellet"></div><div class="member-name">Marina Kellet</div></div>
  <div class="member abs" style="left:352px"><div class="member-photo" style="background:linear-gradient(160deg,#6a5a3a,#c89a7a 55%,#8a4a5a)" role="img" aria-label="Portrait of Rosa Tembley"></div><div class="member-name">Rosa Tembley</div></div>
  <div class="member abs active" style="left:616px"><div class="member-photo" style="background:linear-gradient(160deg,#c82a2a,#7a4a3a 55%,#2a3a8a)" role="img" aria-label="Portrait of Dorla Penn"></div><div class="member-name">Dorla Penn</div></div>
  <div class="member abs" style="left:880px"><div class="member-photo" style="background:linear-gradient(160deg,#4a3aa8,#8a3ab0 55%,#5a2a8a)" role="img" aria-label="Portrait of Wade Marlow"></div><div class="member-name">Wade Marlow</div></div>
</section>

<section>
  <div class="join abs" role="img" aria-label="Misty mountain valley with a red flower in the foreground"></div>
  <h2 class="join-text abs">Join us, and be a part of<br>the global effort to find a cure<br>for lorem ipsum!</h2>
  <div class="signup abs"><span class="signup-field abs">name@meadowmail.org</span><div class="btn btn-purple">Send</div></div>
</section>

<section>
  <div class="contact-band abs"></div>
  <svg class="abs" style="left:88px;top:2790px" width="70" height="60" viewBox="0 0 70 60" fill="none" stroke="#fff" stroke-width="2.5"><path d="M10 8 L20 4 L26 18 L20 22 C22 32 28 38 38 42 L42 36 L56 42 L52 52 C30 52 10 32 10 8Z"/><rect x="34" y="2" width="32" height="22" rx="3"/><path d="M48 9h14M48 16h14"/><circle cx="41" cy="11" r="3"/></svg>
  <div class="contact-title abs">Contact Us Now ! + 55 501 442 718</div>
  <div class="contact-sub abs">Lorem ipsum dolor sit amet, consectetur adipiscing elit.</div>
  <div class="btn btn-ghost" style="left:839px;top:2800px;width:128px;height:30px">Contact Us</div>
  <div class="btn btn-red" style="left:983px;top:2800px;width:128px;height:30px">Donate Now!</div>
</section>

<footer>
  <div class="footer abs"></div>
  <div class="foot-link abs" style="left:86px;color:var(--purple)">HOME</div>
  <div class="foot-link abs" style="left:182px">ABOUT US</div>
  <div class="foot-link abs" style="left:305px">PROJECTS</div>
  <div class="foot-link abs" style="left:430px">GET INVOLVED</div>
  <div class="foot-link abs" style="left:577px">CONTACT US</div>
  <div class="foot-copy abs">©2019 Bright Meadow Foundation. &nbsp; I &nbsp; Privacy Policy &nbsp; I &nbsp; Terms</div>
  <div class="social abs" style="left:839px" aria-label="Social link"></div>
  <div class="social abs" style="left:879px;background:var(--purple)" aria-label="Social link"></div>
  <div class="social abs" style="left:919px" aria-label="Social link"></div>
  <div class="social abs" style="left:959px" aria-label="Social link"></div>
  <div class="social abs" style="left:999px" aria-label="Social link"></div>
  <div class="to-top abs"><svg class="abs" style="left:34px;top:70px" width="22" height="22" viewBox="0 0 22 22"><path d="M11 0 L22 22 L11 16 L0 22Z" fill="#fff"/></svg></div>
</footer>

</body>
</html>
```